Book Cover Design Project

We need a book cover for a eBook on internet banking.

This eBook is meant to be an easy to read, practical book to help people understand what internet banking is, the pros and cons and cover the pure 'internet only' banks that have no branches. The intention is to help people to make informed decisions about whether to use internet banking, how to use it safely and explain in detail what 'internet only' banks are and whether they are right for them.

The cover should not look technical so that non-technical people are not scared off by the look. I have uploaded a book cover design that has the style that I am trying to portray, I have also uploaded a front cover that I created but do not think is suitable.

The cover wording layout could be something like
"Internet Banking"
"A practical guide to answer all your questions" or "The ultimate guide to internet banking" or "The Who's What's and How's of Internet Banking"
Authors name : Colin Pettifer

Industry/Entity Type

Internet

```html
<!DOCTYPE html>
<html lang="en">
<head>
<meta charset="utf-8">
<title>Internet Banking – A practical guide</title>
<link rel="stylesheet" href="https://fonts.googleapis.com/css2?family=Fira+Sans+Extra+Condensed:wght@700&family=Arimo:ital,wght@0,400;1,400&display=swap">
<style>
  :root {
    --cover-blue: #0b6399;
    --cover-blue-deep: #08507f;
    --band-blue: #0a7ad2;
    --band-edge: #0866ad;
    --panel-white: #ffffff;
    --panel-frame: #124f86;
    --title-navy: #12507f;
    --title-orange: #f26a10;
    --text-white: #ffffff;
    --photo-light: #eef2e6;
    --photo-green: #9cc85a;
    --photo-soil: #4a3424;
    --photo-gold: #c79a3c;
  }
  html, body {
    margin: 0;
    padding: 0;
    overflow: hidden;
    background: #ffffff;
  }
  .cover {
    position: relative;
    width: 768px;
    height: 1200px;
    overflow: hidden;
    background:
      repeating-linear-gradient(180deg, rgba(255,255,255,0.025) 0 2px, rgba(0,0,0,0) 2px 6px),
      linear-gradient(180deg, var(--cover-blue) 0%, var(--cover-blue) 70%, var(--cover-blue-deep) 100%);
  }
  .hero-photo {
    position: absolute;
    left: 0;
    top: 0;
    width: 768px;
    height: 450px;
    background:
      linear-gradient(180deg, var(--photo-light) 0%, #d6e3c0 18%, var(--photo-green) 30%, var(--photo-soil) 48%, #8b6a34 62%, var(--photo-gold) 82%, #a9823a 100%);
  }
  .mouse-shape {
    position: absolute;
    left: 540px;
    top: 650px;
    width: 260px;
    height: 210px;
    border-radius: 50%;
    background: radial-gradient(ellipse at 45% 40%, rgba(20,110,170,0.55) 0%, rgba(11,99,153,0) 70%);
  }
  .title-panel {
    position: absolute;
    left: 0;
    top: 0;
    width: 768px;
    height: 700px;
  }
  .title {
    position: absolute;
    left: 84px;
    top: 462px;
    width: 620px;
    margin: 0;
    text-align: center;
    font-family: "Fira Sans Extra Condensed", sans-serif;
    font-weight: 700;
    font-size: 88px;
    line-height: 1;
    letter-spacing: 0.5px;
    color: var(--title-navy);
  }
  .title-accent { color: var(--title-orange); }
  .subtitle {
    position: absolute;
    left: 0;
    top: 720px;
    width: 768px;
    margin: 0;
    text-align: center;
    font-family: "Arimo", sans-serif;
    font-weight: 400;
    font-size: 52px;
    line-height: 72px;
    color: var(--text-white);
    text-shadow: 0 2px 3px rgba(0,0,0,0.35);
  }
  .author-band {
    position: absolute;
    left: 0;
    top: 1048px;
    width: 768px;
    height: 88px;
    background: linear-gradient(180deg, #0c84de 0%, var(--band-blue) 60%, var(--band-edge) 100%);
    border-top: 1px solid rgba(255,255,255,0.25);
    border-bottom: 1px solid rgba(0,0,0,0.2);
  }
  .author {
    margin: 0;
    text-align: center;
    font-family: "Arimo", sans-serif;
    font-style: italic;
    font-weight: 400;
    font-size: 46px;
    line-height: 88px;
    letter-spacing: 1px;
    color: var(--text-white);
  }
</style>
</head>
<body>
  <main class="cover">
    <div class="hero-photo" role="img" aria-label="Photo of stacked gold coins topped with soil and green seedlings"></div>
    <div class="mouse-shape" role="img" aria-label="Faint computer mouse"></div>

    <svg class="title-panel" viewBox="0 0 768 700" aria-hidden="true">
      <polygon points="66,360 720,406 716,660 70,660" fill="#0c3c66" opacity="0.35" transform="translate(0,6)"/>
      <polygon points="68,358 722,404 718,654 70,660" fill="var(--panel-frame)"/>
      <polygon points="82,372 708,415 704,630 84,644" fill="var(--panel-white)"/>
    </svg>

    <h1 class="title">Internet <span class="title-accent">Banking</span></h1>

    <p class="subtitle">A practical guide<br>to answer<br>all your questions</p>

    <div class="author-band">
      <p class="author">Colin Pettifer</p>
    </div>
  </main>
</body>
</html>
```